Personal training company in the fitness industry

Training

(Front of card)
Forge Hour Fitness
417 Calloway Street Canningvale 6155 (Inside VelaGym36 complex)
Tomas Halvorsk
Personal Trainer
halvtomas@brentlo.net
0417 203 958
Back of card
One on One Training
Group Training (min 3)
Outdoor bootcamps
Workout programs
Meal guides
Competition preparation
(bottom middle of card)
GET THAT FORGE ON!

```html
<!DOCTYPE html>
<html lang="en">
<head>
<meta charset="utf-8">
<title>Forge Hour Fitness – Business Card</title>
<link rel="stylesheet" href="https://fonts.googleapis.com/css2?family=Cabin:wght@400;600&family=Cinzel:wght@400&family=Cormorant+Garamond:wght@600&display=swap">
<style>
  :root {
    --page: #ffffff;
    --card-dark: #1d1d1d;
    --photo-dark: #2a2a2a;
    --photo-light: #8a8a8a;
    --band-dark: #1a1a1a;
    --band-light: #8c8c8c;
    --text-light: #f4f4f4;
    --text-soft: #e2e2e2;
    --hex-dark: #3c3c3c;
    --hex-light: #6e6e6e;
    --item-text: #2a2a2a;
    --slogan: #303030;
    --rule: #111111;
  }
  * { margin: 0; padding: 0; box-sizing: border-box; }
  html, body { width: 972px; height: 1200px; overflow: hidden; background: var(--page); }
  .sheet { position: relative; width: 972px; height: 1200px; }

  /* Front card */
  .card-front {
    position: absolute; left: 18px; top: 18px; width: 937px; height: 572px;
    background: var(--card-dark); overflow: hidden;
  }
  .photo { position: absolute; top: 0; height: 100%; }
  .photo-man {
    left: 0; width: 340px;
    background: radial-gradient(ellipse at 55% 45%, var(--photo-light) 0%, #5a5a5a 35%, var(--photo-dark) 70%, var(--card-dark) 100%);
  }
  .photo-woman {
    right: 0; width: 260px;
    background: radial-gradient(ellipse at 50% 50%, #9a9a9a 0%, #606060 35%, var(--photo-dark) 70%, var(--card-dark) 100%);
  }
  .band {
    position: absolute; left: 0; width: 100%;
    background: linear-gradient(to bottom, var(--band-dark) 0%, #3a3a3a 22%, var(--band-light) 50%, #3a3a3a 78%, var(--band-dark) 100%);
    opacity: 0.85;
    border-top: 1px solid #a8a8a8; border-bottom: 1px solid #a8a8a8;
  }
  .band-title { top: 112px; height: 88px; }
  .band-address { top: 459px; height: 56px; }
  .brand-name {
    position: absolute; left: 0; width: 100%; top: 120px;
    text-align: center; font-family: "Cabin", sans-serif; font-weight: 400;
    font-size: 60px; line-height: 72px; color: var(--text-light);
  }
  .contact {
    position: absolute; left: 290px; width: 360px; top: 258px;
    text-align: center; font-family: "Cabin", sans-serif; font-size: 25px;
    line-height: 34px; color: var(--text-soft);
  }
  .address {
    position: absolute; left: 0; width: 100%; top: 466px;
    text-align: center; font-family: "Cinzel", serif; font-size: 30px; line-height: 40px;
    color: var(--text-light);
  }
  .address-note {
    position: absolute; left: 0; width: 100%; top: 522px;
    text-align: center; font-family: "Cinzel", serif; font-size: 17px;
    color: var(--text-soft); letter-spacing: 0.5px;
  }

  .divider { position: absolute; left: 0; top: 603px; width: 972px; height: 2px; background: var(--rule); }

  /* Back card */
  .card-back { position: absolute; left: 18px; top: 619px; width: 937px; height: 565px; overflow: hidden; }
  .hex-field {
    position: absolute; inset: 0;
    background: radial-gradient(ellipse at 50% 40%, var(--hex-light) 0%, #555 55%, var(--hex-dark) 100%);
  }
  .pennant { position: absolute; left: 317px; top: 0; width: 300px; height: 351px; }
  .services {
    position: absolute; left: 317px; top: 30px; width: 300px;
    list-style: none; text-align: center;
    font-family: "Cormorant Garamond", serif; font-weight: 600; font-size: 27px;
    color: var(--item-text);
  }
  .services li { height: 48px; line-height: 32px; position: relative; }
  .services li + li::before {
    content: ""; position: absolute; left: 145px; top: -12px; width: 9px; height: 9px;
    background: #222; transform: rotate(45deg);
  }
  .services li.top-item { color: #9a9a9a; }
  .slogan {
    position: absolute; left: 0; top: 390px; width: 937px;
    text-align: center; font-family: "Cabin", sans-serif; font-weight: 600;
    font-size: 78px; line-height: 110px; color: var(--slogan); white-space: nowrap;
  }
</style>
</head>
<body>
<div class="sheet">

  <section class="card-front">
    <div class="photo photo-man" role="img" aria-label="Black and white photo of a muscular male torso"></div>
    <div class="photo photo-woman" role="img" aria-label="Black and white photo of a toned female torso"></div>

    <div class="band band-title"></div>
    <h1 class="brand-name">Forge Hour Fitness</h1>

    <div class="contact">
      <p>Tomas Halvorsk</p>
      <p>Personal Trainer</p>
      <p>halvtomas@brentlo.net</p>
      <p>0417 203 958</p>
    </div>

    <div class="band band-address"></div>
    <p class="address">417 Calloway Street, Marlow Heights 6208</p>
    <p class="address-note">(Inside VelaGym36 complex)</p>
  </section>

  <div class="divider"></div>

  <section class="card-back">
    <div class="hex-field" role="img" aria-label="Grey hexagon mesh background texture"></div>

    <svg class="pennant" viewBox="0 0 300 351" aria-hidden="true">
      <defs>
        <linearGradient id="pennantFill" x1="0" y1="0" x2="0" y2="1">
          <stop offset="0" stop-color="#1a1a1a"/>
          <stop offset="0.35" stop-color="#6a6a6a"/>
          <stop offset="0.75" stop-color="#d8d8d8"/>
          <stop offset="1" stop-color="#f0f0f0"/>
        </linearGradient>
      </defs>
      <polygon points="0,0 300,0 300,275 150,351 0,275" fill="url(#pennantFill)"/>
    </svg>

    <ul class="services">
      <li class="top-item">One on One Training</li>
      <li>Group Training (min 3)</li>
      <li>Outdoor bootcamps</li>
      <li>Workout programs</li>
      <li>Competition preparation</li>
      <li>Meal guides</li>
    </ul>

    <p class="slogan">GET THAT FORGE ON!</p>
  </section>

</div>
</body>
</html>
```